Solvane Holdings Inc. Business Card Design

My business is custom renovations and homes.I would need to have a new business logo created to go along with my company name. The business card should be of a modern style as this is the market I am focused on. I would need my contact information and website posted on the card. I would also like to list a few of the tasks I conduct on the card (such as: Renovations, Additions, Repairs, New Homes, Design, Consultations). On the reverse of the card I currently have just my logo and my motto, "Shaping Fresh Ground". However, I am open to completely changing everything as I am starting a new year and would like to excel further. Any new ideas and suggestions are always welcomed. Thank you.

Target Market(s)

Upscale residential and commercial renovations and builds

Industry/Entity Type

Business

Contact Information for Business Card

I would like the design to be able to be laser cut or burnt onto a wooden business card. I will be creating one option of cards for really loyal customers (wooden) and a second option for the everyday customer (paper).

Font styles to use
Other font styles liked:
• Calibri / anything of mordern taste

Colors
f37122
5c5c5c
474747
ffffff

Requirements
Must have
• I would like the colours of my business to be a sharp orange and grey. I believe this will symbolize a modern style. I am open to other suggestions if this is not suitable for the designers tastes. My contact info as follows:
• Dirk Malsworth
• President
• Solvane Holdings Inc.
• 555-239-7814
• dirk@solvaneholdings.example
• I would like my website (currently under construction) solvaneholdings.example on the card aswell.
Nice to have
• Along with a modern logo representing Solvane, I would like something on the card besides the logo and contact information. Perhaps a small background design. I feel it may be nice to have my services listed on the card (in smaller font on the bottom) Renovations, Additions, Repairs, Design, Consultations.
Should not have
• The business card should not have too many different colors. Should not have rounded corners.

```html
<!DOCTYPE html>
<html lang="en">
<head>
<meta charset="utf-8">
<title>Solvane Holdings Inc. — Business Card</title>
<link rel="stylesheet" href="https://fonts.googleapis.com/css2?family=Open+Sans:ital,wght@0,400;0,600;1,400&display=swap">
<style>
  :root {
    --orange: #f37122;
    --grey: #5c5c5c;
    --grey-dark: #474747;
    --white: #ffffff;
    --card-dark: #1c1c1c;
    --backdrop: #d3dcdf;
    --light-text: #c9c9c9;
  }
  * { box-sizing: border-box; margin: 0; padding: 0; }
  html, body {
    width: 1000px; height: 1200px; overflow: hidden;
    background: var(--backdrop);
    font-family: "Open Sans", Arial, sans-serif;
  }
  .canvas { position: relative; width: 1000px; height: 1200px; }

  .card {
    position: absolute; left: 209px; width: 567px;
    border-radius: 18px; overflow: hidden;
  }
  .card-front { top: 75px; height: 348px; background: var(--white); }
  .card-back { top: 562px; height: 334px; background: var(--card-dark); }

  .brand { position: absolute; text-align: center; }
  .brand-square { display: block; margin: 0 auto; background: var(--orange); }
  .brand-name { display: block; font-weight: 400; letter-spacing: -0.5px; line-height: 1; }

  .card-front .brand { left: 47px; top: 116px; width: 200px; }
  .card-front .brand-square { width: 60px; height: 60px; }
  .card-front .brand-name { margin-top: 22px; font-size: 44px; color: var(--grey-dark); }

  .divider {
    position: absolute; left: 270px; top: 102px;
    width: 3px; height: 161px; background: var(--orange);
  }
  .contact { position: absolute; left: 293px; top: 113px; }
  .contact-name { font-size: 24px; color: var(--grey-dark); line-height: 1.1; }
  .contact-role { font-size: 14px; color: var(--orange); line-height: 1.2; }
  .contact-list { list-style: none; margin-top: 22px; }
  .contact-list li {
    display: flex; align-items: center; height: 29px;
    font-size: 14.5px; color: var(--grey-dark);
  }
  .contact-list svg { width: 16px; height: 16px; margin-right: 11px; flex: none; }

  .card-back .brand { left: 0; top: 46px; width: 567px; }
  .card-back .brand-square { width: 72px; height: 72px; }
  .card-back .brand-name { margin-top: 20px; font-size: 54px; color: var(--light-text); }
  .motto {
    position: absolute; left: 0; top: 228px; width: 567px; text-align: center;
    font-style: italic; font-size: 17px; color: var(--orange);
  }
  .services {
    position: absolute; left: 0; top: 282px; width: 567px; text-align: center;
    font-size: 15px; color: #e6e6e6; list-style: none;
  }
  .services li { display: inline; }
  .services li + li::before { content: "|"; color: var(--orange); margin: 0 9px; }

  .brand-standalone { left: 0; top: 968px; width: 1000px; }
  .brand-standalone .brand-square { width: 80px; height: 80px; }
  .brand-standalone .brand-name { margin-top: 30px; font-size: 62px; color: var(--grey-dark); }
</style>
</head>
<body>
<main class="canvas">

  <section class="card card-front" aria-label="Business card front">
    <div class="brand">
      <span class="brand-square"></span>
      <span class="brand-name">Solvane</span>
    </div>
    <div class="divider"></div>
    <div class="contact">
      <p class="contact-name">Dirk Malsworth</p>
      <p class="contact-role">President</p>
      <ul class="contact-list">
        <li>
          <svg viewBox="0 0 16 16" aria-hidden="true"><path fill="#f37122" d="M1 6c0-2 3-3 7-3s7 1 7 3v1h-3V5.5C11 5 5 5 4 5.5V7H1zM4 8l1.5-2h5L12 8v5H4z"/><circle cx="8" cy="10" r="1.4" fill="#fff"/></svg>
          (555) 239-7814
        </li>
        <li>
          <svg viewBox="0 0 16 16" aria-hidden="true"><rect x="1" y="3.5" width="14" height="9" fill="#f37122"/><path d="M1 3.5l7 5 7-5M1 12.5l5-4.5M15 12.5l-5-4.5" fill="none" stroke="#fff" stroke-width="1"/></svg>
          dirk@solvaneholdings.example
        </li>
        <li>
          <svg viewBox="0 0 16 16" aria-hidden="true"><g fill="none" stroke="#f37122" stroke-width="1"><circle cx="8" cy="8" r="6.5"/><ellipse cx="8" cy="8" rx="2.8" ry="6.5"/><path d="M1.5 8h13M2.5 4.8h11M2.5 11.2h11"/></g></svg>
          solvaneholdings.example
        </li>
      </ul>
    </div>
  </section>

  <section class="card card-back" aria-label="Business card back">
    <div class="brand">
      <span class="brand-square"></span>
      <span class="brand-name">Solvane</span>
    </div>
    <p class="motto">Shaping Fresh Ground</p>
    <ul class="services">
      <li>Renovations</li><li>Additions</li><li>Repairs</li><li>Design</li><li>Consultations</li>
    </ul>
  </section>

  <div class="brand brand-standalone">
    <span class="brand-square"></span>
    <span class="brand-name">Solvane</span>
  </div>

</main>
</body>
</html>
```